Realty Group Needs Classy, Contemporary Letterhead Design

We need a letterhead design for a new realty company located in NY, USA. We buy investment properties to rehabilitate and or keep in our rental portfolio.

```html
<!DOCTYPE html>
<html lang="en">
<head>
<meta charset="utf-8">
<title>Meridian Realty Group – Stationery</title>
<link href="https://fonts.googleapis.com/css2?family=Montserrat:wght@700&family=Open+Sans:wght@400;600&display=swap" rel="stylesheet">
<style>
  :root {
    --brand-purple: #4a2a82;
    --paper: #ffffff;
    --backdrop: #e9e9eb;
    --ink: #4a4a4a;
    --rule: #9a9a9a;
    --signature-tone: #ececef;
  }
  * { box-sizing: border-box; margin: 0; padding: 0; }
  html, body { width: 1200px; height: 800px; overflow: hidden; }
  body {
    background: var(--backdrop);
    font-family: "Open Sans", Arial, sans-serif;
    color: var(--ink);
    position: relative;
  }

  /* Letterhead */
  .letterhead {
    position: absolute;
    left: 70px; top: 25px;
    width: 530px; height: 750px;
    background: var(--paper);
    box-shadow: 0 4px 14px rgba(0,0,0,0.12);
    padding: 48px 52px 40px;
  }
  .brand-mark {
    display: flex; align-items: center; gap: 8px;
    justify-content: flex-end;
  }
  .brand-mark__dot {
    width: 14px; height: 14px; border-radius: 50%;
    background: var(--brand-purple);
  }
  .brand-mark__name {
    font-family: "Montserrat", Arial, sans-serif;
    font-weight: 700;
    color: var(--brand-purple);
    font-size: 20px;
    letter-spacing: 0.5px;
  }
  .letter-body {
    margin-top: 34px;
    font-size: 10.5px;
    line-height: 1.6;
  }
  .letter-body p { margin-bottom: 12px; }
  .signature-space {
    width: 90px; height: 46px;
    background: var(--signature-tone);
    margin-top: 10px;
  }
  .letter-footer {
    position: absolute;
    left: 52px; right: 52px; bottom: 38px;
    font-size: 11px;
    line-height: 1.7;
    border-top: 1px solid #dedede;
    padding-top: 12px;
  }
  .contact-row { display: flex; flex-wrap: wrap; gap: 4px 16px; align-items: center; }
  .contact-item { display: inline-flex; align-items: center; gap: 5px; }
  .contact-icon { width: 11px; height: 11px; fill: var(--brand-purple); flex: none; }

  /* Business cards */
  .business-card {
    position: absolute;
    width: 220px; height: 385px;
    box-shadow: 0 4px 12px rgba(0,0,0,0.14);
  }
  .business-card--front {
    left: 660px; top: 200px;
    background: var(--paper);
    padding: 40px 22px 30px;
  }
  .business-card--back {
    left: 920px; top: 200px;
    background: var(--brand-purple);
    display: flex; flex-direction: column;
    align-items: center; justify-content: center;
  }
  .business-card .brand-mark { justify-content: center; }
  .business-card .brand-mark__name { font-size: 13px; text-align: center; }
  .business-card--back .brand-mark__name { color: var(--paper); }
  .business-card--back .brand-mark__dot { background: var(--paper); width: 10px; height: 10px; }
  .business-card--front .brand-mark__dot { width: 10px; height: 10px; }
  .card-person { margin-top: 90px; }
  .card-person__name {
    font-family: "Montserrat", Arial, sans-serif;
    font-weight: 700; font-size: 12px;
    color: var(--brand-purple);
    text-transform: uppercase;
  }
  .card-person__title { font-weight: 600; font-size: 10.5px; color: #333; }
  .card-contact { margin-top: 18px; font-size: 9.5px; line-height: 1.65; }
  .card-contact .contact-icon { width: 9px; height: 9px; }
  .card-web {
    position: absolute; bottom: 34px;
    color: var(--paper); font-size: 10px;
  }
</style>
</head>
<body>

<article class="letterhead">
  <header class="brand-mark">
    <span class="brand-mark__dot"></span>
    <span class="brand-mark__name">Meridian Realty Group, LLC</span>
  </header>

  <section class="letter-body">
    <p>Dear customer,</p>
    <p>Lorem ipsum dolor sit amet, consectetur adipisicing elit, sed do eiusmod tempor incididunt ut labore et dolore magna aliqua. Ut enim ad minim veniam, quis nostrud exercitation ullamco laboris nisi ut aliquip ex ea commodo consequat. Duis aute irure dolor in reprehenderit in voluptate velit esse cillum dolore eu fugiat nulla pariatur. Excepteur sint occaecat cupidatat non proident, sunt in culpa qui officia deserunt mollit anim id est laborum.</p>
    <p>Lorem ipsum dolor sit amet, consectetur adipisicing elit, sed do eiusmod tempor incididunt ut labore et dolore magna aliqua. Ut enim ad minim veniam, quis nostrud exercitation ullamco laboris nisi ut aliquip ex ea commodo consequat. Duis aute irure dolor in reprehenderit in voluptate velit esse cillum dolore eu fugiat nulla pariatur. Excepteur sint occaecat cupidatat non proident, sunt in culpa qui officia deserunt mollit anim id est laborum.</p>
    <p>Lorem ipsum dolor sit amet, consectetur adipisicing elit, sed do eiusmod tempor incididunt ut labore et dolore magna aliqua. Ut enim ad minim veniam, quis nostrud exercitation ullamco laboris nisi ut aliquip ex ea commodo consequat. Duis aute irure dolor in reprehenderit in voluptate velit esse cillum dolore eu fugiat nulla pariatur. Excepteur sint occaecat cupidatat non proident, sunt in culpa qui officia deserunt mollit anim id est laborum.</p>
    <p>Lorem ipsum dolor sit amet, consectetur adipisicing elit, sed do eiusmod tempor incididunt ut labore et dolore magna aliqua. Ut enim ad minim veniam, quis nostrud exercitation ullamco laboris nisi ut aliquip ex ea commodo consequat. Duis aute irure dolor in reprehenderit.</p>
    <p>Yours Sincerely,</p>
    <div class="signature-space" role="img" aria-label="Handwritten signature of the sender"></div>
  </section>

  <footer class="letter-footer">
    <div>48 Harbor View Lane, Kingston, NY 12401</div>
    <div class="contact-row">
      <span class="contact-item">
        <svg class="contact-icon" viewBox="0 0 24 24"><path d="M6.6 10.8a15.1 15.1 0 0 0 6.6 6.6l2.2-2.2a1 1 0 0 1 1-.25 11.4 11.4 0 0 0 3.6.57 1 1 0 0 1 1 1V20a1 1 0 0 1-1 1A17 17 0 0 1 3 4a1 1 0 0 1 1-1h3.5a1 1 0 0 1 1 1c0 1.25.2 2.45.57 3.57a1 1 0 0 1-.25 1z"/></svg>
        555.204.7810
      </span>
      <span class="contact-item">
        <svg class="contact-icon" viewBox="0 0 24 24"><path d="M2 5h20v14H2z M2 5l10 8 10-8" fill="none" stroke="currentColor" stroke-width="0"/><path d="M2 5h20v2l-10 7L2 7z"/><path d="M2 9l10 7 10-7v10H2z"/></svg>
        info@meridianrealty.com
      </span>
      <span class="contact-item">
        <svg class="contact-icon" viewBox="0 0 24 24"><circle cx="12" cy="12" r="10"/></svg>
        www.meridianrealty.com
      </span>
    </div>
  </footer>
</article>

<section class="business-card business-card--front">
  <div class="brand-mark">
    <span class="brand-mark__dot"></span>
    <span class="brand-mark__name">Meridian Realty Group, LLC</span>
  </div>
  <div class="card-person">
    <div class="card-person__name">Daniel Ashworth</div>
    <div class="card-person__title">Managing Director</div>
  </div>
  <div class="card-contact">
    <div>48 Harbor View Lane,<br>Kingston, NY 12401</div>
    <div class="contact-item">
      <svg class="contact-icon" viewBox="0 0 24 24"><path d="M6.6 10.8a15.1 15.1 0 0 0 6.6 6.6l2.2-2.2a1 1 0 0 1 1-.25 11.4 11.4 0 0 0 3.6.57 1 1 0 0 1 1 1V20a1 1 0 0 1-1 1A17 17 0 0 1 3 4a1 1 0 0 1 1-1h3.5a1 1 0 0 1 1 1c0 1.25.2 2.45.57 3.57a1 1 0 0 1-.25 1z"/></svg>
      555.204.7810
    </div><br>
    <div class="contact-item">
      <svg class="contact-icon" viewBox="0 0 24 24"><path d="M2 5h20v2l-10 7L2 7z"/><path d="M2 9l10 7 10-7v10H2z"/></svg>
      info@meridianrealty.com
    </div><br>
    <div class="contact-item">
      <svg class="contact-icon" viewBox="0 0 24 24"><circle cx="12" cy="12" r="10"/></svg>
      www.meridianrealty.com
    </div>
  </div>
</section>

<section class="business-card business-card--back">
  <div class="brand-mark">
    <span class="brand-mark__dot"></span>
    <span class="brand-mark__name">Meridian Realty Group, LLC</span>
  </div>
  <div class="card-web">www.meridianrealty.com</div>
</section>

</body>
</html>
```